Need Business cards

Im a new realtor and already have a logo. I would like to purchase a Business card design that catches customer's attention, its creative, and modern.

Marisol Quintero
Realtor ®
(555) 318 4027
marisolqtrhomes@brindlemail.com

Target Market(s)

investors, buyers and seller, property management

Industry/Entity Type

real estate,

Contact Information for Business Card

Marisol Quintero

Requirements
Must have
• BOTH LOGOS, WOULD LIKE TO SEE WITH DIFFERENT OPTIONS WITH EITHER PICTURE

```html
<!DOCTYPE html>
<html lang="en">
<head>
<meta charset="utf-8">
<title>Marisol Quintero – Realtor Business Card</title>
<link href="https://fonts.googleapis.com/css2?family=Montserrat:wght@500;600;700&display=swap" rel="stylesheet">
<style>
  :root {
    --gold-deep: #b8861a;
    --gold: #d4a32c;
    --gold-light: #f2d160;
    --white: #ffffff;
    --backdrop: #e9e6e1;
    --photo-a: #efe3c8;
    --photo-b: #d9c39a;
  }
  * { margin: 0; padding: 0; box-sizing: border-box; }
  html, body { width: 900px; height: 1200px; overflow: hidden; }
  body {
    background: var(--backdrop);
    font-family: "Montserrat", sans-serif;
    position: relative;
  }
  .card {
    position: absolute;
    left: 80px;
    width: 738px;
    height: 432px;
    background: var(--white);
    border-radius: 12px 42px 12px 42px;
    overflow: hidden;
    box-shadow: 0 6px 18px rgba(0,0,0,0.18);
  }
  .card--front { top: 133px; }
  .card--back { top: 642px; }

  /* Front */
  .front__band {
    position: absolute;
    left: 0; top: 0;
    width: 100%; height: 220px;
    background: linear-gradient(100deg, var(--gold-deep) 0%, var(--gold) 45%, var(--gold-light) 100%);
  }
  .front__stripe {
    position: absolute;
    left: 0; top: 226px;
    width: 352px; height: 8px;
    background: linear-gradient(90deg, var(--gold-deep), var(--gold-light));
  }
  .front__photo {
    position: absolute;
    right: 28px; top: 28px;
    width: 218px; height: 404px;
    background: linear-gradient(160deg, var(--photo-a), var(--photo-b));
    border-radius: 8px 8px 0 0;
  }
  .agent {
    position: absolute;
    left: 30px; top: 50px;
    color: var(--white);
  }
  .agent__name {
    font-size: 26px;
    font-weight: 700;
    letter-spacing: 0.3px;
    line-height: 1;
  }
  .agent__title {
    font-size: 18px;
    font-weight: 500;
    margin-top: 10px;
    letter-spacing: 0.5px;
  }
  .agent__rule {
    width: 295px;
    height: 1px;
    background: rgba(255,255,255,0.7);
    margin: 14px 0 10px;
  }
  .contact {
    list-style: none;
    font-size: 17px;
    font-weight: 500;
  }
  .contact li {
    display: flex;
    align-items: center;
    gap: 10px;
    height: 28px;
  }
  .contact svg { width: 18px; height: 18px; fill: var(--white); }
  .brokerage {
    position: absolute;
    left: 30px; top: 340px;
    font-size: 30px;
    font-weight: 700;
    color: var(--gold-deep);
    letter-spacing: 0.5px;
  }

  /* Back */
  .back__mark {
    position: absolute;
    left: 289px; top: 96px;
    width: 160px; height: 160px;
    border: 6px solid var(--gold);
    display: flex;
    align-items: center;
    justify-content: center;
    font-size: 56px;
    font-weight: 700;
    color: var(--gold);
    letter-spacing: 2px;
  }
  .back__identity {
    position: absolute;
    left: 0; right: 0; top: 286px;
    text-align: center;
    color: var(--gold);
  }
  .back__name {
    font-size: 22px;
    font-weight: 700;
    letter-spacing: 0.8px;
  }
  .back__title {
    display: flex;
    align-items: center;
    justify-content: center;
    gap: 12px;
    font-size: 15px;
    font-weight: 600;
    letter-spacing: 1px;
    margin-top: 4px;
  }
  .back__title::before,
  .back__title::after {
    content: "";
    width: 72px;
    height: 1.5px;
    background: var(--gold);
  }
  .back__wave {
    position: absolute;
    left: 0; bottom: 0;
    width: 738px; height: 90px;
  }
</style>
</head>
<body>

<section class="card card--front">
  <div class="front__band"></div>
  <div class="front__stripe"></div>
  <div class="front__photo" role="img" aria-label="Portrait photograph of the realtor"></div>

  <div class="agent">
    <h1 class="agent__name">MARISOL QUINTERO</h1>
    <p class="agent__title">REALTOR ®</p>
    <div class="agent__rule"></div>
    <ul class="contact">
      <li>
        <svg viewBox="0 0 24 24" aria-hidden="true"><path d="M6.6 10.8a15.1 15.1 0 0 0 6.6 6.6l2.2-2.2c.3-.3.7-.4 1-.2 1.1.4 2.3.6 3.6.6.6 0 1 .4 1 1V20c0 .6-.4 1-1 1A17 17 0 0 1 3 4c0-.6.4-1 1-1h3.5c.6 0 1 .4 1 1 0 1.3.2 2.5.6 3.6.1.3 0 .7-.2 1z"/></svg>
        (555) 318 4027
      </li>
      <li>
        <svg viewBox="0 0 24 24" aria-hidden="true"><path d="M2 5h20v14H2zm2 2v.4l8 5 8-5V7zm0 2.8V17h16V9.8l-8 5z"/></svg>
        marisolqtrhomes@brindlemail.com
      </li>
    </ul>
  </div>

  <p class="brokerage">KEYSTRIDE REALTY</p>
</section>

<section class="card card--back">
  <div class="back__mark" role="img" aria-label="Personal monogram logo of the realtor">MQ</div>
  <div class="back__identity">
    <h2 class="back__name">MARISOL QUINTERO</h2>
    <p class="back__title">REALTOR</p>
  </div>
  <svg class="back__wave" viewBox="0 0 738 90" preserveAspectRatio="none" aria-hidden="true">
    <defs>
      <linearGradient id="waveGold" x1="0" x2="1" y1="0" y2="0">
        <stop offset="0" stop-color="#b8861a"/>
        <stop offset="0.5" stop-color="#d9ab35"/>
        <stop offset="1" stop-color="#f2d160"/>
      </linearGradient>
    </defs>
    <path d="M0 32 C 180 20, 330 20, 470 46 S 680 58, 738 28 L 738 90 L 0 90 Z" fill="url(#waveGold)"/>
  </svg>
</section>

</body>
</html>
```